Create for us a Shop-Stopper Business Card

We need a standout, first class business card to go along with our new brand strategy. Sleek, Contemporary and fresh.

Colors and theme must sync with our websitewww.pelvorpower.co.uk

We want a business card that has a global brand appeal. TKR Energy is a small UK renewable company that specialises in energy projects in Africa. We want a business card that has the following characteristics: Very short, precise, global, stand out, NOT TOO LOUD but contemporary. The company's colour themes are White, Grey with a hint of green.

Target Market(s)

Business exec, high net worth individuals, investors, commercial leaders, suppliers, government officials

Industry/Entity Type

Solar Energy

Contact Information for Business Card

Logo, Name, Title, Address, web address, email,

Requirements
Must have
• Logo must be sharp
Nice to have
• Adapt fonts from the logo. The large circular side of the logo at the back in a very refreshing way
Should not have
• No solar panel shapes or image.Very little black. If possible avoid black. Its not coming out nice. I think !!!

```html
<!DOCTYPE html>
<html lang="en">
<head>
<meta charset="utf-8">
<title>TKR Energy Business Card</title>
<link href="https://fonts.googleapis.com/css2?family=Montserrat:wght@600;700&family=Roboto:wght@400;500&display=swap" rel="stylesheet">
<style>
  :root {
    --stage-centre: #23683a;
    --stage-edge: #12391f;
    --card-white: #ffffff;
    --brand-green: #0d7a3e;
    --leaf-green: #7cc242;
    --text-grey: #4a4a4a;
    --wordmark-grey: #3a3a3a;
    --rule-red: #c8272d;
    --faint-grey: #f1f2f1;
  }
  html, body {
    margin: 0;
    width: 1200px;
    height: 900px;
    overflow: hidden;
  }
  body {
    background: radial-gradient(ellipse at 50% 50%, var(--stage-centre), var(--stage-edge) 75%);
    font-family: "Roboto", Arial, sans-serif;
    position: relative;
  }
  .card {
    position: absolute;
    width: 600px;
    height: 340px;
    background: var(--card-white);
    border-radius: 22px;
    overflow: hidden;
    box-shadow: 0 18px 40px rgba(0, 0, 0, 0.35);
  }
  .card--back { left: 110px; top: 80px; }
  .card--front { left: 490px; top: 480px; }

  .back-disc {
    position: absolute;
    right: -70px;
    top: -60px;
    width: 380px;
    height: 380px;
    border-radius: 50%;
    background: var(--brand-green);
  }
  .back-name {
    position: absolute;
    right: 30px;
    top: 110px;
    width: 260px;
    text-align: center;
    font-family: "Montserrat", Arial, sans-serif;
    font-weight: 600;
    font-size: 34px;
    color: var(--card-white);
    letter-spacing: 1px;
  }
  .back-web {
    position: absolute;
    left: 30px;
    bottom: 24px;
    font-size: 12px;
    font-weight: 500;
    letter-spacing: 1.5px;
    color: var(--brand-green);
  }

  .front-halo {
    position: absolute;
    left: 30px;
    top: 30px;
    width: 330px;
    height: 330px;
    border-radius: 50%;
    background: var(--faint-grey);
  }
  .wordmark {
    position: absolute;
    left: 36px;
    top: 180px;
    display: flex;
    align-items: center;
    gap: 10px;
  }
  .wordmark-dot {
    width: 34px;
    height: 34px;
    border-radius: 50%;
    background: var(--brand-green);
  }
  .wordmark-name {
    font-family: "Montserrat", Arial, sans-serif;
    font-weight: 600;
    font-size: 28px;
    color: var(--wordmark-grey);
    letter-spacing: 0.5px;
  }
  .wordmark-rule {
    position: absolute;
    left: 80px;
    top: 222px;
    width: 200px;
    height: 2px;
    background: var(--rule-red);
  }
  .details {
    position: absolute;
    left: 330px;
    top: 44px;
    color: var(--text-grey);
    font-size: 12px;
    letter-spacing: 1.2px;
    line-height: 1.5;
  }
  .person-name {
    font-family: "Montserrat", Arial, sans-serif;
    font-weight: 700;
    font-size: 26px;
    color: var(--leaf-green);
    letter-spacing: 0.5px;
    line-height: 1.1;
    margin: 0;
  }
  .person-title { margin: 2px 0 18px; }
  .address { margin: 0 0 18px; }
  .contact-list { list-style: none; margin: 0; padding: 0; }
  .contact-list li { display: flex; align-items: center; gap: 10px; }
  .contact-list svg { width: 12px; height: 12px; flex: none; }
</style>
</head>
<body>
  <section class="card card--back">
    <div class="back-disc"></div>
    <div class="back-name">TKR Energy</div>
    <div class="back-web">www.pelvorpower.co.uk</div>
  </section>

  <section class="card card--front">
    <div class="front-halo"></div>
    <div class="wordmark">
      <span class="wordmark-dot"></span>
      <span class="wordmark-name">TKR Energy</span>
    </div>
    <div class="wordmark-rule"></div>

    <div class="details">
      <h1 class="person-name">Arin Vale</h1>
      <p class="person-title">Manager</p>
      <p class="address">Halvert Park Complex<br>Northbay, Aldmoor 40218</p>
      <ul class="contact-list">
        <li>
          <svg viewBox="0 0 12 12" aria-hidden="true"><rect x="3" y="1" width="6" height="10" rx="1" fill="none" stroke="#7cc242" stroke-width="1.5"/></svg>
          120 4455 318
        </li>
        <li>
          <svg viewBox="0 0 12 12" aria-hidden="true"><rect x="1" y="2.5" width="10" height="7" fill="none" stroke="#7cc242" stroke-width="1.3"/><path d="M1 2.5 6 7 11 2.5" fill="none" stroke="#7cc242" stroke-width="1.3"/></svg>
          info@pelvorpower.co.uk
        </li>
        <li>
          <svg viewBox="0 0 12 12" aria-hidden="true"><circle cx="6" cy="6" r="5" fill="#7cc242"/><path d="M1 6h10M6 1c2 2.5 2 7.5 0 10M6 1c-2 2.5-2 7.5 0 10" fill="none" stroke="#fff" stroke-width="0.9"/></svg>
          www.pelvorpower.co.uk
        </li>
      </ul>
    </div>
  </section>
</body>
</html>
```